" Trabalhamos com palha italiana de vários sabores. Estamos começando agora entao no momento trabalhamos com encomendas e vendas boca a boca www.redevizinha.com/docelume "

```html
<!DOCTYPE html>
<html lang="pt-BR">
<head>
<meta charset="utf-8">
<title>Doce Lume — cartão de visita</title>
<link rel="stylesheet" href="https://fonts.googleapis.com/css2?family=Open+Sans:wght@400;600;700&display=swap">
<style>
  :root {
    --backdrop: #e4e4e2;
    --cream: #f3e6c6;
    --teal: #6fb8a4;
    --peach: #f2b27a;
    --coral: #d96b55;
    --cocoa: #5a3a2b;
    --cocoa-deep: #2e1a12;
    --cocoa-mid: #4a2c1f;
    --ink-light: #f6efe6;
  }
  * { box-sizing: border-box; margin: 0; padding: 0; }
  html, body {
    width: 1200px; height: 1200px; overflow: hidden;
    background: var(--backdrop);
    font-family: "Open Sans", Arial, sans-serif;
  }
  .sheet {
    width: 1200px; height: 1200px;
    display: flex; flex-direction: column;
    align-items: center; justify-content: center; gap: 40px;
  }
  .card {
    position: relative;
    width: 900px; height: 515px;
    border-radius: 6px; overflow: hidden;
    box-shadow: 0 10px 28px rgba(0,0,0,.18);
  }

  /* Back side: contact */
  .card--contact .food-photo {
    position: absolute; inset: 0;
    background:
      radial-gradient(ellipse at 70% 40%, #6b4330 0%, var(--cocoa-mid) 40%, transparent 75%),
      linear-gradient(135deg, var(--cocoa-deep) 0%, #3b2218 50%, var(--cocoa-mid) 100%);
  }
  .contact {
    position: absolute; left: 150px; top: 70px;
    color: var(--ink-light);
  }
  .contact__name {
    font-weight: 600; font-size: 28px; margin-bottom: 26px; letter-spacing: .3px;
  }
  .contact__row {
    display: flex; align-items: flex-start; gap: 12px;
    font-size: 20px; line-height: 1.3; margin-bottom: 12px;
  }
  .contact__row svg { flex: none; width: 20px; height: 20px; margin-top: 3px; }
  .brand--light {
    position: absolute; right: 70px; top: 215px;
    display: flex; align-items: center; gap: 12px;
    color: var(--ink-light);
  }

  /* Front side: brand */
  .card--brand .pattern {
    position: absolute; inset: 0;
    background:
      radial-gradient(circle at 15% 20%, var(--teal) 0%, transparent 30%),
      radial-gradient(circle at 85% 15%, var(--peach) 0%, transparent 32%),
      radial-gradient(circle at 20% 85%, var(--coral) 0%, transparent 30%),
      radial-gradient(circle at 88% 80%, var(--teal) 0%, transparent 30%),
      radial-gradient(circle at 50% 50%, var(--cream) 0%, var(--cream) 35%, #e7cfa4 100%);
  }
  .brand--dark {
    position: absolute; left: 50%; top: 50%;
    transform: translate(-50%, -50%);
    display: flex; align-items: center; gap: 16px;
    color: var(--cocoa);
  }
  .brand__name {
    font-weight: 700; white-space: nowrap;
  }
  .brand--light .brand__name { font-size: 40px; }
  .brand--dark .brand__name { font-size: 84px; }
  .brand__dot {
    border-radius: 50%; background: currentColor; flex: none;
  }
  .brand--light .brand__dot { width: 14px; height: 14px; }
  .brand--dark .brand__dot { width: 26px; height: 26px; }
</style>
</head>
<body>
<main class="sheet">

  <section class="card card--contact">
    <div class="food-photo" role="img" aria-label="Fotografia escura de palha italiana de chocolate em close"></div>
    <div class="contact">
      <p class="contact__name">Marina Solano</p>
      <p class="contact__row">
        <svg viewBox="0 0 20 20" fill="currentColor" aria-hidden="true"><path d="M10 1a6 6 0 0 0-6 6c0 4.5 6 12 6 12s6-7.5 6-12a6 6 0 0 0-6-6zm0 8.3A2.3 2.3 0 1 1 10 4.7a2.3 2.3 0 0 1 0 4.6z"/></svg>
        <span>Rua das Acácias, 418<br>7º andar, Vila Clara<br>Campo Verde - SP | CEP: 01230-000</span>
      </p>
      <p class="contact__row">
        <svg viewBox="0 0 20 20" fill="currentColor" aria-hidden="true"><path d="M5 2l3 4-2 2a11 11 0 0 0 6 6l2-2 4 3-2 3C9 18 2 11 2 4z"/></svg>
        <span>Tel: 11 - 4000 2222<br>11 - 94000 2233</span>
      </p>
      <p class="contact__row">
        <svg viewBox="0 0 20 20" fill="none" stroke="currentColor" stroke-width="1.8" aria-hidden="true"><rect x="2" y="4" width="16" height="12" rx="1.5"/><path d="M2.5 5l7.5 6 7.5-6"/></svg>
        <span>encomenda@docelume.com.br</span>
      </p>
      <p class="contact__row">
        <svg viewBox="0 0 20 20" fill="none" stroke="currentColor" stroke-width="1.6" aria-hidden="true"><circle cx="10" cy="10" r="8"/><path d="M2 10h16M10 2c3 3 3 13 0 16M10 2c-3 3-3 13 0 16"/></svg>
        <span>www.redevizinha.com/docelume</span>
      </p>
    </div>
    <div class="brand brand--light">
      <span class="brand__dot"></span>
      <span class="brand__name">Doce Lume</span>
    </div>
  </section>

  <section class="card card--brand">
    <div class="pattern" role="img" aria-label="Padrão decorativo de cápsulas arredondadas em verde, pêssego, coral e marrom sobre creme"></div>
    <div class="brand brand--dark">
      <span class="brand__dot"></span>
      <span class="brand__name">Doce Lume</span>
    </div>
  </section>

</main>
</body>
</html>
```